Bold Website Design for Fitness Trainer - No Coding

We are in need of a bold and unique website design for a personal fitness training company, www.TessaLorvel.com. We need DESIGN ONLY for three pages. These will be a homepage, a lead capture page, and one internal page with a sidebar. The design will be used for coding a wordpress theme, if that matters for the designer.

Tessa Lorvel Fitness Training
2738 E 19th St #415
Austin, TX 78705
512-607-4918
http://www.tessalorvel.com

Target Market(s)

18-45 year old male and females making 80k+ a year and looking to get stronger and in shape.

Industry/Entity Type

Fitness

Number of Pages Required

3 page

Font styles to use
Sans Serif

Requirements
Must have
• See attached design specs file.
Nice to have
Should not have
• Boxed layout.
• Dark Background.

```html
<!DOCTYPE html>
<html lang="en">
<head>
<meta charset="utf-8">
<title>Tessa Lorvel Fitness Training</title>
<link href="https://fonts.googleapis.com/css2?family=Lato:wght@400;700;900&family=Open+Sans:wght@400;600;700&display=swap" rel="stylesheet">
<style>
:root{
  --cyan:#1ca3e0;
  --cyan-dark:#1589bf;
  --yellow:#f5cf14;
  --ink:#1f2a33;
  --text:#5b6770;
  --muted:#9aa4ab;
  --line:#e3e7ea;
  --slate:#3d5668;
  --slate-dark:#2c4252;
  --footer:#1995cf;
  --footer-bar:#0f3a55;
  --white:#fff;
}
*{box-sizing:border-box;margin:0;padding:0}
html,body{width:1200px;height:3224px;overflow:hidden}
body{position:relative;background:var(--white);font-family:"Open Sans",Arial,sans-serif;color:var(--text);font-size:13px;line-height:1.6}
h1,h2,h3,h4{font-family:"Lato",Arial,sans-serif;color:var(--ink)}
a{color:inherit;text-decoration:none}

/* header */
.site-header{position:absolute;top:0;left:0;width:1200px;height:120px;background:var(--white);z-index:2}
.brand{position:absolute;left:80px;top:30px;display:flex;align-items:center;gap:14px}
.brand-mark{width:58px;height:58px;border-radius:50%;background:var(--yellow)}
.brand-name{font-family:"Lato",sans-serif;font-weight:900;font-size:32px;color:var(--ink)}
.main-nav{position:absolute;right:70px;top:16px;display:flex;gap:22px;align-items:center;font-family:"Lato",sans-serif;font-weight:700;font-size:12px;color:var(--ink);letter-spacing:.5px}
.main-nav .active{border-bottom:2px solid var(--cyan);padding-bottom:3px}
.main-nav .free{border:1px solid var(--cyan);color:var(--cyan);padding:4px 10px}
.utility{position:absolute;right:70px;top:66px;display:flex;gap:22px;align-items:center;font-size:12px;color:var(--ink);font-weight:600}
.utility span{display:flex;align-items:center;gap:7px}
.socials{display:flex;gap:5px}
.socials i{display:block;width:22px;height:22px;border-radius:3px}

/* hero */
.hero{position:absolute;top:120px;left:0;width:1200px;height:470px;background:linear-gradient(100deg,#dfe3e6 0%,#c8ced3 40%,#a9b2b9 70%,#d7dbde 100%)}
.hero-caption{position:absolute;left:0;top:220px;width:430px;height:195px;background:rgba(28,163,224,.85);padding:26px 28px;color:var(--white)}
.hero-caption h1{color:var(--white);font-size:26px;font-weight:900;line-height:1.2;text-transform:uppercase}
.hero-caption p{font-size:12px;line-height:1.55;margin-top:12px}
.hero-dots{position:absolute;right:24px;bottom:22px;display:flex;gap:5px}
.hero-dots i{width:11px;height:11px;background:rgba(255,255,255,.6)}
.hero-dots i:first-child{background:var(--white)}

/* cta band */
.cta-band{position:absolute;top:590px;left:0;width:1200px;height:142px;display:flex}
.cta-band .half{flex:1;display:flex;align-items:center;justify-content:center}
.cta-band .yellow{background:var(--yellow)}
.cta-band .blue{background:var(--cyan)}
.btn-dark{background:#111;color:var(--white);font-family:"Lato",sans-serif;font-weight:700;font-size:15px;padding:16px 0;width:230px;text-align:center;text-transform:uppercase;letter-spacing:.5px}

/* section headings */
.section-title{position:absolute;left:0;width:1200px;text-align:center;font-size:22px;font-weight:700;text-transform:uppercase;letter-spacing:.5px}
.section-title b{color:var(--cyan);font-size:30px;margin:0 16px;font-weight:400}

/* services */
.services{position:absolute;top:880px;left:130px;width:940px;display:flex}
.service{flex:1;text-align:center;padding:0 40px;border-left:1px solid var(--line)}
.service:first-child{border-left:0}
.service-icon{width:92px;height:92px;border-radius:50%;background:#e9ecee;border:3px solid #d4d9dc;margin:0 auto 18px;display:flex;align-items:center;justify-content:center}
.service h3{font-size:17px;font-weight:900;text-transform:uppercase}
.service p{font-size:12.5px;margin:6px 0 14px;line-height:1.5}
.btn-small{display:inline-block;background:var(--cyan);color:var(--white);font-size:11px;padding:5px 14px}

/* testimonials */
.testimonials{position:absolute;top:1232px;left:0;width:1200px;height:322px;background:linear-gradient(180deg,var(--slate) 0%,var(--slate-dark) 100%);text-align:center;color:#e5ecf1}
.testimonials h2{color:var(--white);font-size:21px;font-weight:700;margin-top:52px;text-transform:uppercase}
.stats{display:flex;justify-content:center;gap:12px;margin-top:18px}
.stats span{background:#1f3341;color:var(--white);font-size:13px;padding:8px 18px}
.quote{position:absolute;left:232px;top:165px;display:flex;align-items:center;gap:22px;text-align:left;width:820px}
.avatar{width:98px;height:98px;border-radius:50%;background:linear-gradient(160deg,#d8c2a8,#8c7560);border:4px solid #fff;flex:none}
.quote p{font-size:13px;line-height:1.5}
.arrow{position:absolute;top:150px;width:30px;height:30px}

/* widgets */
.social-feed{position:absolute;top:1570px;left:0;width:1200px;height:360px;background:#f1f2f3}
.widget{position:absolute;background:var(--white);border:1px solid #cfd4d8;box-shadow:0 2px 6px rgba(0,0,0,.12);font-size:10px;color:var(--ink)}
.widget-head{background:#eef0f3;border-bottom:1px solid #d8dde2;padding:6px 10px;font-weight:700;font-size:11px}
.feed-row{display:flex;gap:8px;padding:6px 10px;align-items:center;border-bottom:1px solid #f0f0f0;line-height:1.3}
.thumb{width:26px;height:26px;background:#b9c3cb;flex:none}
.grid{display:grid;grid-template-columns:repeat(4,48px);gap:5px;padding:8px 10px}
.grid i{height:44px;background:linear-gradient(135deg,#9aa7b1,#c9d0d6)}

/* blog */
.post{position:absolute;left:186px;width:930px;height:222px}
.post-img{position:absolute;top:0;width:440px;height:222px;background:linear-gradient(120deg,#c9ced2,#8f9aa2 60%,#d7cbc2)}
.post-body{position:absolute;top:0;width:450px}
.meta{display:flex;gap:16px;font-size:10px;color:var(--muted)}
.meta span::before{content:"";display:inline-block;width:8px;height:8px;background:#c4ccd2;margin-right:5px;vertical-align:-1px}
.post h3{font-family:"Open Sans",sans-serif;font-size:14px;font-weight:600;margin:12px 0 6px}
.post p{font-size:12px;line-height:1.55}
.more{display:inline-flex;align-items:center;gap:6px;color:var(--cyan);font-size:12px;margin-top:10px}

/* footer */
.site-footer{position:absolute;top:2874px;left:0;width:1200px;height:266px;background:var(--footer);color:var(--white)}
.site-footer h4{color:var(--white);font-size:13px;font-weight:900;text-transform:uppercase;margin-bottom:12px}
.col{position:absolute;top:50px;font-size:12px;line-height:1.75}
.map{position:absolute;left:543px;top:40px;width:290px;height:135px;background:linear-gradient(135deg,#e4eef4,#c7dbe7)}
.contact{display:flex;gap:10px;align-items:flex-start;margin-bottom:10px;line-height:1.5}
.contact svg{flex:none;margin-top:3px}
.footer-bar{position:absolute;top:3140px;left:0;width:1200px;height:84px;background:var(--footer-bar);color:#cfe3ef;font-size:12px;display:flex;align-items:center;justify-content:center}
</style>
</head>
<body>

<header class="site-header">
  <a class="brand" href="#"><span class="brand-mark"></span><span class="brand-name">Tessa Lorvel</span></a>
  <nav class="main-nav">
    <a class="active">HOME</a><a>PROGRAMS</a><a>MEET YOUR TRAINER</a><a>BLOG</a><a>CONTACT ME</a><a class="free">FREE SESSION</a>
  </nav>
  <div class="utility">
    <span><svg width="14" height="14" viewBox="0 0 14 14"><path d="M3 1l3 3-2 2c1 2 2 3 4 4l2-2 3 3-2 2C6 13 1 8 1 3z" fill="#1f2a33"/></svg>(000) 000-0000</span>
    <span><svg width="12" height="14" viewBox="0 0 12 14"><path d="M6 0a5 5 0 0 1 5 5c0 4-5 9-5 9S1 9 1 5a5 5 0 0 1 5-5z" fill="#1f2a33"/><circle cx="6" cy="5" r="2" fill="#fff"/></svg>Locations</span>
    <span><svg width="14" height="14" viewBox="0 0 14 14"><rect x="1" y="2" width="12" height="11" fill="none" stroke="#1f2a33" stroke-width="1.6"/><path d="M1 5h12" stroke="#1f2a33" stroke-width="1.6"/></svg>Appointment</span>
    <span class="socials"><i style="background:#3b5a9a"></i><i style="background:#dd4b39"></i><i style="background:#e52d27"></i><i style="background:#cb2027"></i><i style="background:#517fa4"></i></span>
  </div>
</header>

<section class="hero" role="img" aria-label="Trainer coaching a client on an exercise bike in a bright gym">
  <div class="hero-caption">
    <h1>Lorem ipsum dolor<br>sit amet consectetur...</h1>
    <p>Lorem ipsum dolor sit amet, consectetur adipiscing elit. Aenean nisi eros eleifend vitae accumsan sit amet, efficitur mollis mauris. Nunc tellus odio, commodo feugiat tortor non.</p>
  </div>
  <div class="hero-dots"><i></i><i></i></div>
</section>

<section class="cta-band">
  <div class="half yellow"><a class="btn-dark">Call to Action</a></div>
  <div class="half blue"><a class="btn-dark">Get Started Today</a></div>
</section>

<h2 class="section-title" style="top:800px"><b>/</b>Our Services<b>/</b></h2>
<section class="services">
  <article class="service">
    <div class="service-icon"><svg width="48" height="40" viewBox="0 0 48 40"><path d="M6 30c0-10 8-18 18-18s18 8 18 18z" fill="none" stroke="#1f2a33" stroke-width="3"/><path d="M24 30l8-10" stroke="#1f2a33" stroke-width="3"/></svg></div>
    <h3>Personal Training</h3>
    <p>Lorem ipsum dolor sit amet, consectetur adipiscing elit. Aenean nisi eros.</p>
    <a class="btn-small">Read More</a>
  </article>
  <article class="service">
    <div class="service-icon"><svg width="48" height="40" viewBox="0 0 48 40"><rect x="9" y="6" width="30" height="20" fill="none" stroke="#1f2a33" stroke-width="3"/><path d="M4 32h40" stroke="#1f2a33" stroke-width="3"/></svg></div>
    <h3>Online Coaching</h3>
    <p>Lorem ipsum dolor sit amet, consectetur adipiscing elit. Aenean nisi eros.</p>
    <a class="btn-small">Read More</a>
  </article>
  <article class="service">
    <div class="service-icon"><svg width="48" height="40" viewBox="0 0 48 40"><path d="M10 30L38 10" stroke="#1f2a33" stroke-width="3"/><rect x="4" y="26" width="10" height="10" fill="#1f2a33" transform="rotate(-35 9 31)"/><rect x="34" y="4" width="10" height="10" fill="#1f2a33" transform="rotate(-35 39 9)"/></svg></div>
    <h3>Strength Programming</h3>
    <p>Lorem ipsum dolor sit amet, consectetur adipiscing elit. Aenean nisi eros.</p>
    <a class="btn-small">Read More</a>
  </article>
</section>

<section class="testimonials" aria-label="Testimonials">
  <h2>What People Say About Us</h2>
  <div class="stats"><span>1124 Customer Reviews</span><span>95 % Growth</span><span>24 Countries</span></div>
  <svg class="arrow" style="left:70px" viewBox="0 0 30 30"><path d="M19 6l-9 9 9 9" fill="none" stroke="#fff" stroke-width="3"/></svg>
  <svg class="arrow" style="right:70px" viewBox="0 0 30 30"><path d="M11 6l9 9-9 9" fill="none" stroke="#fff" stroke-width="3"/></svg>
  <div class="quote">
    <div class="avatar" role="img" aria-label="Client portrait"></div>
    <p>Lorem ipsum dolor sit amet, consectetur adipiscing elit. Aliquam elementum bibendum lectus, in maximus mi facilisis vel. Suspendisse cursus varius lorem, eu facilisis velit vulputate sit.</p>
  </div>
</section>

<section class="social-feed" aria-label="Social activity">
  <div class="widget" style="left:321px;top:72px;width:270px;height:232px">
    <div class="widget-head">Recent Activity</div>
    <div class="feed-row"><i class="thumb"></i><span><b>Mara Quill</b> shared a new training photo with her group</span></div>
    <div class="feed-row"><i class="thumb"></i><span><b>Dena Forsel</b> liked a post about morning workouts</span></div>
    <div class="feed-row"><i class="thumb"></i><span><b>Joel Brandt</b> commented on a strength program</span></div>
    <div class="feed-row"><i class="thumb"></i><span>Weekly fitness tips now posted for members</span></div>
  </div>
  <div class="widget" style="left:596px;top:58px;width:282px;height:250px">
    <div class="widget-head">Tessa Lorvel Fitness Training</div>
    <div class="feed-row"><i class="thumb"></i><span>1,240 people follow this page</span></div>
    <div class="grid"><i></i><i></i><i></i><i></i><i></i><i></i><i></i><i></i></div>
    <div class="feed-row"><i class="thumb" style="width:14px;height:14px"></i><span>Follow page</span></div>
  </div>
</section>

<h2 class="section-title" style="top:2010px"><b>/</b>Latest Blog Posts<b>/</b></h2>

<article class="post" style="top:2092px">
  <div class="post-img" style="left:0" role="img" aria-label="Trainer assisting a woman lifting weights"></div>
  <div class="post-body" style="left:458px">
    <div class="meta"><span>Site Admin</span><span>March 17, 2015</span><span>0 Comments</span><span>Leave a comment</span></div>
    <h3>Lorem ipsum dolor sit amet, consectetur adipiscing</h3>
    <p>Lorem ipsum dolor sit amet, consectetur adipiscing elit. Aenean nisi eros, eleifend vitae accumsan sit amet, efficitur mollis mauris. Nunc tellus odio, commodo feugiat tortor non, dignissim tristique sem. Etiam consequat leo suscipit elit auctor.</p>
    <a class="more"><svg width="14" height="10"><path d="M0 5h11M7 1l4 4-4 4" stroke="#1ca3e0" stroke-width="2" fill="none"/></svg>Read More</a>
  </div>
</article>

<article class="post" style="top:2346px">
  <div class="post-body" style="left:-100px">
    <div class="meta"><span>Site Admin</span><span>March 17, 2015</span><span>0 Comments</span><span>Leave a comment</span></div>
    <h3>Lorem ipsum dolor sit amet, consectetur adipiscing</h3>
    <p>Lorem ipsum dolor sit amet, consectetur adipiscing elit. Aenean nisi eros, eleifend vitae accumsan sit amet, efficitur mollis mauris. Nunc tellus odio, commodo feugiat tortor non, dignissim tristique sem. Etiam consequat leo suscipit elit auctor.</p>
    <a class="more"><svg width="14" height="10"><path d="M0 5h11M7 1l4 4-4 4" stroke="#1ca3e0" stroke-width="2" fill="none"/></svg>Read More</a>
  </div>
  <div class="post-img" style="left:384px" role="img" aria-label="Two people training with dumbbells"></div>
</article>

<article class="post" style="top:2596px">
  <div class="post-img" style="left:0" role="img" aria-label="Trainer guiding a client on a treadmill"></div>
  <div class="post-body" style="left:458px">
    <div class="meta"><span>Site Admin</span><span>March 17, 2015</span><span>0 Comments</span><span>Leave a comment</span></div>
    <h3>Lorem ipsum dolor sit amet, consectetur adipiscing</h3>
    <p>Lorem ipsum dolor sit amet, consectetur adipiscing elit. Aenean nisi eros, eleifend vitae accumsan sit amet, efficitur mollis mauris. Nunc tellus odio, commodo feugiat tortor non, dignissim tristique sem. Etiam consequat leo suscipit elit auctor.</p>
    <a class="more"><svg width="14" height="10"><path d="M0 5h11M7 1l4 4-4 4" stroke="#1ca3e0" stroke-width="2" fill="none"/></svg>Read More</a>
  </div>
</article>

<footer class="site-footer">
  <div class="col" style="left:86px">
    <h4>Resources Links</h4>
    <div style="display:flex;gap:60px"><div>Home<br>Programs<br>Meet Your Trainer</div><div>Blog<br>Contact Me</div></div>
  </div>
  <div class="col" style="left:350px">
    <h4>Social Media Links</h4>
    <div class="socials"><i style="background:#fff"></i><i style="background:#fff"></i><i style="background:#fff"></i><i style="background:#fff"></i><i style="background:#fff"></i></div>
  </div>
  <div class="map" role="img" aria-label="Map showing the studio location"></div>
  <div class="col" style="left:905px;width:250px">
    <h4>Connect With Us</h4>
    <div class="contact"><svg width="12" height="16" viewBox="0 0 12 14"><path d="M6 0a5 5 0 0 1 5 5c0 4-5 9-5 9S1 9 1 5a5 5 0 0 1 5-5z" fill="#fff"/></svg><span>Studio Address Line One<br>City Name, State 00000</span></div>
    <div class="contact"><svg width="14" height="14" viewBox="0 0 14 14"><path d="M3 1l3 3-2 2c1 2 2 3 4 4l2-2 3 3-2 2C6 13 1 8 1 3z" fill="#fff"/></svg><span>(000) 000-0000, (000) 000-0000</span></div>
    <div class="contact"><svg width="14" height="12" viewBox="0 0 14 12"><rect x="1" y="1" width="12" height="10" fill="none" stroke="#fff" stroke-width="1.6"/><path d="M1 1l6 5 6-5" stroke="#fff" stroke-width="1.6" fill="none"/></svg><span>info@tessalorvel.com</span></div>
  </div>
</footer>
<div class="footer-bar">© 2015 - Tessa Lorvel. All rights reserved. Terms of Use | Privacy Policy</div>

</body>
</html>
```